Business Card for Brightvale Homestead Care

I need a business card design for a very elite and personalized companion care company. We take care of the client at home with respect, dignity, and our full attention. The design should communicate a classic elegance and trust.

```html
<!DOCTYPE html>
<html lang="en">
<head>
<meta charset="utf-8">
<title>Brightvale Homestead Care – Business Card</title>
<link href="https://fonts.googleapis.com/css2?family=Open+Sans:wght@400;600;700&display=swap" rel="stylesheet">
<style>
  :root {
    --navy: #0b4a80;
    --navy-deep: #08416f;
    --sky: #2fa3dc;
    --ink: #1e1e1e;
    --paper: #f7f7f7;
    --stage: #e4e5e7;
  }
  * { margin: 0; padding: 0; box-sizing: border-box; }
  html, body {
    width: 1200px; height: 1021px; overflow: hidden;
    background: var(--stage);
    font-family: "Open Sans", Arial, sans-serif;
  }
  .card {
    position: absolute;
    width: 630px; height: 360px;
    box-shadow: 0 10px 28px rgba(0,0,0,.18);
  }
  .card-back {
    left: 470px; top: 110px;
    background: var(--navy);
  }
  .card-front {
    left: 100px; top: 550px;
    background: var(--paper);
  }
  .wordmark {
    position: absolute;
    display: flex; align-items: center; gap: 12px;
    font-weight: 600;
    text-transform: uppercase;
    letter-spacing: .06em;
    line-height: 1.15;
  }
  .wordmark-dot {
    width: 16px; height: 16px; border-radius: 50%;
    background: var(--sky); flex: none;
  }
  .card-back .wordmark {
    right: 44px; bottom: 52px;
    color: #ffffff; font-size: 30px;
  }
  .card-front .wordmark {
    left: 40px; top: 40px;
    color: var(--navy); font-size: 30px;
  }
  .person {
    position: absolute; left: 44px; top: 150px;
  }
  .person-name {
    font-size: 22px; font-weight: 700; color: var(--navy);
  }
  .person-role {
    font-size: 17px; color: var(--ink); margin-top: -2px;
  }
  .contact {
    position: absolute; left: 44px; top: 232px;
    list-style: none; font-size: 17px; color: var(--ink); line-height: 24px;
  }
  .contact li { display: flex; align-items: center; gap: 8px; }
  .contact svg { width: 16px; height: 16px; flex: none; }
  .contact .address { margin-top: 4px; }
</style>
</head>
<body>

<section class="card card-back" aria-label="Card back">
  <div class="wordmark"><span class="wordmark-dot"></span>Brightvale<br>Homestead Care</div>
</section>

<section class="card card-front" aria-label="Card front">
  <div class="wordmark"><span class="wordmark-dot"></span>Brightvale<br>Homestead Care</div>

  <div class="person">
    <p class="person-name">Daniel Harrow</p>
    <p class="person-role">President</p>
  </div>

  <ul class="contact">
    <li>
      <svg viewBox="0 0 16 16" fill="none" stroke="#2fa3dc" stroke-width="1.4"><rect x="4" y="1" width="8" height="14" rx="1.5"/><line x1="7" y1="12.5" x2="9" y2="12.5"/></svg>
      555-214-3080
    </li>
    <li>
      <svg viewBox="0 0 16 16" fill="none" stroke="#2fa3dc" stroke-width="1.4"><rect x="1" y="3" width="14" height="10"/><polyline points="1,3 8,9 15,3"/></svg>
      daniel@brightvalecare.com
    </li>
    <li>
      <svg viewBox="0 0 16 16" fill="none" stroke="#2fa3dc" stroke-width="1.3"><circle cx="8" cy="8" r="6.5"/><ellipse cx="8" cy="8" rx="3" ry="6.5"/><line x1="1.5" y1="8" x2="14.5" y2="8"/></svg>
      www.brightvalecare.com
    </li>
    <li class="address">418 Linden Crest Lane Harbor Vale, FL 34021</li>
  </ul>
</section>

</body>
</html>
```